Electrical Contracting business website design

Website needed to help promote an online footprint focused on local customers in my area Gympie, QLD,Australia 4570

I am after a clear website (one where my customer does not get lost or frustrated)
most important is to engage customer to Call now or Request a quote with all the lead details.

Some bread and butter work for us is broken hot water units, electrical faults and renovators

We offer all sorts of services
- smoke alarms
- Test n Tag
- Lighting
- Fans
- A/C
- Design and planning
- safety switches
- underground Power
- Energy efficient solutions
- hot water repair
- Fault finding
- Control / Automation

Target Market(s)

Local Customers, Renovators, Builders, Commercial, Industrial, Domestic

Industry/Entity Type

Electrician

Coding

Coded - Design and coding required

Number of Pages Required

1 page

Colors
f78f20
000000
ec1f27
ffffff

Requirements
Must have
• Easy to use website with clear Contact Information (call now button)
• Ph: 0491527308 24/7
• Email Brightvoltservices@examplemail.com
• , Quote request to receive leads and customer info

```html
<!DOCTYPE html>
<html lang="en">
<head>
<meta charset="utf-8">
<title>Brightvolt Electrical</title>
<link rel="stylesheet" href="https://fonts.googleapis.com/css2?family=Poppins:wght@300;400;500;600;700&display=swap">
<style>
:root{
  --orange:#f78f20;
  --red:#ec1f27;
  --black:#000000;
  --white:#ffffff;
  --ink:#1a1a1a;
  --muted:#555555;
  --light:#f5f5f5;
  --dark:#1b1e22;
}
*{box-sizing:border-box;margin:0;padding:0}
html,body{width:1200px;height:3651px;overflow:hidden}
body{position:relative;background:var(--white);font-family:'Poppins',sans-serif;color:var(--ink)}
.abs{position:absolute}
.btn{position:absolute;display:flex;align-items:center;justify-content:center;color:var(--white);font-size:11px;font-weight:600;letter-spacing:.3px;text-transform:uppercase;border-radius:2px}
.btn-red{background:var(--red)}
.btn-orange{background:var(--orange)}
.btn-black{background:var(--black)}
.hl{color:var(--red)}

/* header */
.brand{left:88px;top:30px;display:flex;align-items:center;gap:10px;font-size:20px;font-weight:700;color:var(--red);line-height:1.1}
.brand .mark{width:18px;height:18px;background:var(--orange)}
.support{left:723px;top:22px;font-size:15px;font-weight:600;color:var(--red);display:flex;align-items:center;gap:6px}
.support b{color:var(--black);font-weight:600}
.nav{top:62px;font-size:13px;color:var(--ink)}
.nav.active{color:var(--red)}

/* hero */
.hero{left:0;top:95px;width:1200px;height:465px;background:linear-gradient(100deg,#3a3f44 0%,#5b6166 45%,#6f7478 70%,#4a4f53 100%)}
.hero-title{left:88px;top:215px;color:var(--white);font-size:40px;line-height:1.12;font-weight:300}
.hero-title b{font-weight:600;display:block}
.hero-text{left:88px;top:322px;width:470px;color:var(--white);font-size:17px;font-weight:300;line-height:24px}
.dots-v{left:1099px;top:261px;display:flex;flex-direction:column;gap:10px}
.dots-v i,.dots-h i{display:block;width:11px;height:11px;border:1.5px solid var(--white);border-radius:50%}
.dots-v i.on,.dots-h i.on{background:radial-gradient(circle,var(--white) 35%,transparent 40%)}
.callbar{z-index:5;left:602px;top:521px;width:510px;height:78px;background:var(--white);border:3px solid var(--orange);border-top:none;border-radius:0 0 6px 6px;display:flex;align-items:center;padding-left:56px;font-size:16px;color:var(--red);box-shadow:0 6px 14px rgba(0,0,0,.08);white-space:nowrap}
.callbar .num{font-weight:600;margin-left:10px}
.callbar .or{margin:0 24px 0 28px;color:var(--muted)}

/* section titles */
.sec-title{left:0;width:1200px;display:flex;justify-content:center;align-items:center;gap:24px;font-size:28px;font-weight:600;color:var(--black)}
.sec-title::before,.sec-title::after{content:"";width:64px;height:2px;background:var(--orange)}
.sec-title.on-red{color:var(--white)}
.sec-title.on-red::before,.sec-title.on-red::after{background:var(--white)}

/* services */
.services-bg{left:0;top:560px;width:1200px;height:796px;background:var(--light)}
.card{position:absolute;width:320px;height:235px}
.card .photo{position:absolute;left:0;top:0;width:320px;height:200px}
.card .label{position:absolute;left:80px;right:0;top:201px;height:34px;background:var(--orange);color:var(--black);font-size:14px;font-weight:600;display:flex;align-items:center;justify-content:flex-end;padding-right:14px}
.card.active .label{background:var(--red);color:var(--white)}
.card svg.hex{position:absolute;left:40px;top:166px}

/* about */
.about-h{left:88px;top:1433px;font-size:28px;font-weight:600;display:flex;align-items:center;gap:22px}
.about-h::after{content:"";width:64px;height:2px;background:var(--red)}
.about-sub{left:88px;top:1490px;width:460px;font-size:20px;line-height:23px;color:var(--black)}
.about-p{left:88px;width:480px;font-size:12.5px;line-height:19px;color:var(--muted)}
.about-photo{left:601px;top:1356px;width:511px;height:511px;background:linear-gradient(160deg,#4e6a3a 0%,#6b7d57 40%,#30435f 75%,#555a5e 100%)}

/* testimonials */
.testi{left:0;top:1867px;width:1200px;height:457px;background:linear-gradient(180deg,#ec1f27,#e01b23)}
.avatar{left:562px;top:1995px;width:76px;height:76px;border-radius:50%;border:3px solid var(--orange);background:var(--white);display:flex;align-items:center;justify-content:center}
.avatar span{width:62px;height:62px;border-radius:50%;background:linear-gradient(160deg,#c7b6a4,#8a6c55)}
.quote{left:270px;top:2090px;width:660px;text-align:center;color:var(--white);font-size:16.5px;line-height:24px}
.who{left:0;width:1200px;text-align:center;color:var(--white)}
.dots-h{left:562px;top:2243px;display:flex;gap:3px}

/* blog */
.post{position:absolute;width:320px}
.post .photo{height:208px}
.post .box{position:absolute;left:32px;top:146px;width:255px;height:155px;background:var(--white);box-shadow:0 4px 16px rgba(0,0,0,.08);text-align:center;padding:36px 30px 0}
.post .date{font-size:11px;font-weight:600;color:var(--red)}
.post .ttl{margin-top:14px;font-size:14px;font-weight:500;line-height:17px;color:var(--black)}
.post.active .ttl{text-decoration:underline}

/* cta */
.cta{left:0;top:2890px;width:1200px;height:159px;background:var(--orange)}
.cta-q{left:88px;top:2934px;font-size:16px;font-weight:600;line-height:24px;color:var(--black)}
.cta-s{left:528px;top:2940px;font-size:16px;font-weight:600;color:var(--black)}
.cta-n{left:528px;top:2962px;font-size:32px;font-weight:300;color:var(--black)}

/* footer */
.foot-l{left:0;top:3049px;width:601px;height:520px;background:linear-gradient(180deg,#15181c,#2b3036)}
.foot-r{left:601px;top:3049px;width:599px;height:520px;background:var(--light)}
.foot-brand{left:208px;top:3130px;display:flex;align-items:center;gap:10px;font-size:20px;font-weight:700;color:var(--red)}
.foot-brand .mark{width:18px;height:18px;background:var(--orange)}
.foot-call{left:208px;top:3208px;font-size:24px;color:var(--red)}
.foot-t{left:208px;font-size:13px;line-height:19px;color:var(--white)}
.foot-lbl{color:var(--red);font-weight:600}
.social{top:3469px;width:30px;height:30px;border-radius:50%;background:var(--orange)}
.social.on{background:var(--white)}
.quote-h{left:670px;top:3110px;font-size:20px;font-weight:600;color:var(--red)}
.field{position:absolute;left:670px;width:322px;background:var(--white);border:1px solid #ececec;font-size:11px;color:#999;padding:10px 14px}
.copy{left:0;top:3600px;width:1200px;text-align:center;font-size:12px;color:var(--muted)}
</style>
</head>
<body>

<!-- Header -->
<div class="abs brand"><span class="mark"></span>Brightvolt Electrical</div>
<div class="abs support">24/7 Support:
  <svg width="12" height="16" viewBox="0 0 12 16"><rect x="1" y="1" width="10" height="14" rx="1.5" fill="none" stroke="#ec1f27" stroke-width="1.6"/></svg>
  <b>0491 527 308</b></div>
<div class="btn btn-red" style="left:985px;top:17px;width:127px;height:28px">Get a Quote</div>
<div class="abs nav active" style="left:489px">-- Home --</div>
<div class="abs nav" style="left:615px">About Us</div>
<div class="abs nav" style="left:724px">Services</div>
<div class="abs nav" style="left:829px">Testimonials</div>
<div class="abs nav" style="left:961px">Blog</div>
<div class="abs nav" style="left:1039px">Contact Us</div>

<!-- Hero -->
<div class="abs hero" role="img" aria-label="Photo of an electrician in safety glasses working on a switchboard"></div>
<h1 class="abs hero-title">Welcome to<b>Brightvolt Electrical</b></h1>
<p class="abs hero-text">Lorem Ipsum is simply dummy text of the printing and typesetting industry standard.</p>
<div class="btn btn-orange" style="left:88px;top:401px;width:127px;height:29px">Discover More</div>
<div class="abs dots-v"><i></i><i class="on"></i><i></i><i></i></div>

<!-- Services -->
<div class="abs services-bg"></div>
<div class="abs callbar">Call Today!
  <svg style="margin-left:16px" width="17" height="17" viewBox="0 0 24 24"><path d="M5 3h4l2 5-2.5 1.5a11 11 0 0 0 6 6L16 13l5 2v4a2 2 0 0 1-2 2A16 16 0 0 1 3 5a2 2 0 0 1 2-2z" fill="none" stroke="#ec1f27" stroke-width="1.8"/></svg>
  <span class="num">0491 527 308</span><span class="or">or</span>
  <span class="btn btn-red" style="position:static;width:120px;height:31px">Contact Us</span></div>
<h2 class="abs sec-title" style="top:656px"><span>Our <span class="hl">Services</span></span></h2>

<div class="card" style="left:88px;top:727px">
  <div class="photo" role="img" aria-label="Smoke alarm on a ceiling with smoke" style="background:linear-gradient(135deg,#e9e9ea,#cfcfd2)"></div>
  <div class="label">Smoke Alarms</div>
  <svg class="hex" width="82" height="70" viewBox="0 0 82 70"><polygon points="20,0 62,0 82,35 62,70 20,70 0,35" fill="#000"/><circle cx="41" cy="35" r="14" fill="none" stroke="#f78f20" stroke-width="2"/><circle cx="41" cy="35" r="5" fill="none" stroke="#f78f20" stroke-width="2"/></svg>
</div>
<div class="card active" style="left:441px;top:727px">
  <div class="photo" role="img" aria-label="Hands testing a circuit breaker panel with a multimeter" style="background:linear-gradient(135deg,#8a97a6,#c2c6c9 55%,#d4a23a)"></div>
  <div class="label">Test and Tag</div>
  <svg class="hex" width="82" height="70" viewBox="0 0 82 70"><polygon points="20,0 62,0 82,35 62,70 20,70 0,35" fill="#fff"/><rect x="32" y="20" width="14" height="18" rx="3" fill="none" stroke="#ec1f27" stroke-width="2"/><path d="M39 38v8q0 6 8 6h6" fill="none" stroke="#ec1f27" stroke-width="2"/></svg>
</div>
<div class="card" style="left:792px;top:727px">
  <div class="photo" role="img" aria-label="Warmly lit living room with ceiling downlights" style="background:linear-gradient(135deg,#5a4332,#a27a54 55%,#d2b48d)"></div>
  <div class="label">Lighting</div>
  <svg class="hex" width="82" height="70" viewBox="0 0 82 70"><polygon points="20,0 62,0 82,35 62,70 20,70 0,35" fill="#000"/><path d="M28 20h26M41 20v8M31 44l10-16 10 16z" fill="none" stroke="#f78f20" stroke-width="2"/></svg>
</div>
<div class="card" style="left:88px;top:992px">
  <div class="photo" role="img" aria-label="Ceiling fan with wooden blades in a bright room" style="background:linear-gradient(135deg,#dfe2e6,#b6bcc3)"></div>
  <div class="label">Fans Repair</div>
  <svg class="hex" width="82" height="70" viewBox="0 0 82 70"><polygon points="20,0 62,0 82,35 62,70 20,70 0,35" fill="#000"/><circle cx="41" cy="30" r="11" fill="none" stroke="#f78f20" stroke-width="2"/><path d="M41 41v9M33 51h16" stroke="#f78f20" stroke-width="2"/></svg>
</div>
<div class="card" style="left:441px;top:992px">
  <div class="photo" role="img" aria-label="Wall mounted air conditioner unit" style="background:linear-gradient(135deg,#cdc9c2,#f1efec 60%,#b9b4ad)"></div>
  <div class="label">Air Conditioner</div>
  <svg class="hex" width="82" height="70" viewBox="0 0 82 70"><polygon points="20,0 62,0 82,35 62,70 20,70 0,35" fill="#000"/><rect x="24" y="22" width="34" height="16" rx="2" fill="none" stroke="#f78f20" stroke-width="2"/><path d="M30 43v6M36 43v6M42 43v6M48 43v6M54 43v6" stroke="#f78f20" stroke-width="2"/></svg>
</div>
<div class="card" style="left:792px;top:992px">
  <div class="photo" role="img" aria-label="Finger pressing a safety switch in a switchboard" style="background:linear-gradient(135deg,#bfc3c6,#8f9599 50%,#2f7f4f)"></div>
  <div class="label">Safety Switches</div>
  <svg class="hex" width="82" height="70" viewBox="0 0 82 70"><polygon points="20,0 62,0 82,35 62,70 20,70 0,35" fill="#000"/><path d="M41 18v16M31 34h20l-2 16H33z" fill="none" stroke="#f78f20" stroke-width="2"/></svg>
</div>
<div class="btn btn-red" style="left:520px;top:1260px;width:160px;height:31px">View All Services</div>

<!-- About -->
<h2 class="abs about-h"><span>About <span class="hl">Us</span></span></h2>
<p class="abs about-sub">We repair broken hot water units, electrical faults and renovators</p>
<p class="abs about-p" style="top:1554px">There are many variations of passages of Lorem Ipsum available, but the majority have suffered alteration in some form, by injected humour, or randomised words which don't look even slightly believable. If you are going to use a passage of Lorem Ipsum.</p>
<p class="abs about-p" style="top:1649px">Lorem Ipsum is simply dummy text of the printing and typesetting industry. Lorem Ipsum has been the industry's standard dummy text ever since the 1500s, when an unknown printer took a galley ...</p>
<div class="btn btn-orange" style="left:88px;top:1751px;width:127px;height:30px">Discover More</div>
<div class="abs about-photo" role="img" aria-label="Two electricians standing beside a branded work van"></div>

<!-- Testimonials -->
<div class="abs testi" role="img" aria-label="Red tinted photo of a work van on a road"></div>
<h2 class="abs sec-title on-red" style="top:1924px"><span><span style="color:#000">What Our</span> Clients Say</span></h2>
<div class="abs avatar" role="img" aria-label="Client portrait"><span></span></div>
<p class="abs quote">Lorem ipsum dolor sit amet, consectetur adipiscing elit, sed do eiusmod tempor incididunt ut labore et dolore magna aliqua. Ut enim ad minim veniam, quis nostrud exercitation ullamco ...</p>
<div class="abs who" style="top:2183px;font-size:13px;font-weight:600">Jordan Hale</div>
<div class="abs who" style="top:2201px;font-size:10px">Lorem Ipsum</div>
<div class="abs dots-h"><i></i><i class="on"></i><i></i><i></i><i></i></div>

<!-- Blog -->
<h2 class="abs sec-title" style="top:2380px"><span>Latest <span class="hl">Blog</span></span></h2>
<div class="post" style="left:88px;top:2450px">
  <div class="photo" role="img" aria-label="Electrician testing breakers with a multimeter" style="background:linear-gradient(135deg,#6d7378,#c8cbcd 60%,#b53a2a)"></div>
  <div class="box"><div class="date">AUGUST, 14, 2019</div><div class="ttl">There are many lorem passages of lorem Ipsum available work ...</div></div>
</div>
<div class="post active" style="left:441px;top:2450px">
  <div class="photo" role="img" aria-label="Worker in high visibility gear at an industrial switchboard" style="background:linear-gradient(135deg,#9aa3ab,#e38a2c 55%,#3a3d40)"></div>
  <div class="box"><div class="date">AUGUST, 14, 2019</div><div class="ttl">There are many lorem passages of lorem Ipsum available work ...</div></div>
</div>
<div class="post" style="left:792px;top:2450px">
  <div class="photo" role="img" aria-label="Bedroom lit by bedside lamps" style="background:linear-gradient(135deg,#a88a5e,#e2c793 55%,#6b5238)"></div>
  <div class="box"><div class="date">AUGUST, 14, 2019</div><div class="ttl">There are many lorem passages of lorem Ipsum available work ...</div></div>
</div>
<div class="btn btn-red" style="left:536px;top:2794px;width:128px;height:31px">View All Blog</div>

<!-- Call to action -->
<div class="abs cta"></div>
<p class="abs cta-q">Are you having any<br>problems But can't consult to<br>anyone?</p>
<svg class="abs" style="left:366px;top:2910px" width="44" height="120" viewBox="0 0 44 120"><path d="M2 0l40 60-40 60" fill="none" stroke="#c96d10" stroke-width="1.5"/></svg>
<svg class="abs" style="left:447px;top:2936px" width="64" height="64" viewBox="0 0 24 24"><path d="M5 3h4l2 5-2.5 1.5a11 11 0 0 0 6 6L16 13l5 2v4a2 2 0 0 1-2 2A16 16 0 0 1 3 5a2 2 0 0 1 2-2z" fill="none" stroke="#000" stroke-width="1"/><path d="M14 3a7 7 0 0 1 7 7M14 6a4 4 0 0 1 4 4" fill="none" stroke="#000" stroke-width="1"/></svg>
<div class="abs cta-s">24/7 Support</div>
<div class="abs cta-n">0491527308</div>
<svg class="abs" style="left:749px;top:2910px" width="44" height="120" viewBox="0 0 44 120"><path d="M2 0l40 60-40 60" fill="none" stroke="#c96d10" stroke-width="1.5"/></svg>
<div class="btn btn-black" style="left:904px;top:2950px;width:208px;height:39px">Contact Us Today!</div>

<!-- Footer -->
<div class="abs foot-l" role="img" aria-label="Dark photo of a work van among trees at dusk"></div>
<div class="abs foot-r"></div>
<div class="abs foot-brand"><span class="mark"></span>Brightvolt Electrical</div>
<div class="abs foot-call">Call. 0491 527 308</div>
<div class="abs foot-t" style="top:3245px">Brightvoltservices@examplemail.com</div>
<div class="abs foot-t" style="top:3289px"><span class="foot-lbl">Address:</span><br>118 Sample Road Lorem City,<br>Ipsum 45702</div>
<div class="abs foot-t" style="top:3366px"><span class="foot-lbl">Working Hours:</span><br>Monday to Saturday: 9:00 - 18:00<br>Sunday: Closed</div>
<div class="abs social" style="left:209px"></div>
<div class="abs social on" style="left:250px"></div>
<div class="abs social" style="left:292px"></div>
<div class="abs social" style="left:335px"></div>

<h3 class="abs quote-h">Get A Quick Quote</h3>
<div class="field" style="top:3160px;height:33px">Your Name</div>
<div class="field" style="top:3209px;height:34px">Email</div>
<div class="field" style="top:3259px;height:34px">Phone</div>
<div class="field" style="top:3308px;height:135px">Message ...</div>
<div class="btn btn-red" style="left:670px;top:3470px;width:112px;height:30px">Submit</div>

<div class="abs copy">© 2019 <span class="hl">Brightvolt Electrical</span> All Right Reserved</div>
<svg class="abs" style="left:1111px;top:3598px" width="18" height="20" viewBox="0 0 18 20"><path d="M2 19L9 2l7 17M5 12h8" fill="none" stroke="#ec1f27" stroke-width="1.6"/></svg>

</body>
</html>
```